Calendar Ad / Flyer

Our law firm needs a calendar ad to place in a local calendar.
THE DEADLINE IS THIS THURSDAY 06/28/2018.

Attached is the ad used in last years calendar. A few notes on this...
**. This is by no means the model to follow.
Please be creative and do what makes more sense marketing wise.
1. Need to update the color scheme which corresponds to the new website at morvanlegal.net
2. The "MORVAN LEGAL | STANDING FIRM FOR YOUR FUTURE" should be put at the top and made larger
3. "KNOWN AND TRUSTED IN OUR COMMUNITY FOR OVER 21 YEARS" should be changed to "KNOWN AND TRUSTED IN OUR COMMUNITY FOR OVER 22 YEARS"
4. "Dorian K. Morvan, Esq." should be made larger and better positioned.
5. Under the list of practices, it should be changed to have:
"Personal Injury, Legal Malpractice, Unlicensed Contractors, Medical Malpractice, Civil Litigation"
6. Contact information (i.e. contact number, website, and address) should be better positioned
7. Placement of endorsement logos should stand out more.
8. New picture of head attorney is attached.

Last but not least... Give it your best shot!

```html
<!DOCTYPE html>
<html lang="en">
<head>
<meta charset="utf-8">
<title>Morvan Legal – 2018 Calendar Ad</title>
<link rel="stylesheet" href="https://fonts.googleapis.com/css2?family=Outfit:wght@400;500;600;700;800&display=swap">
<style>
:root{
  --gold:#c9a874;
  --gold-deep:#b8935c;
  --gold-band:#d3b583;
  --ink:#111111;
  --white:#ffffff;
  --muted:#b9b6b1;
  --sunday:#e01e2b;
  --photo-a:#9a9ea3;
  --photo-b:#5f6469;
}
*{margin:0;padding:0;box-sizing:border-box}
html,body{width:1200px;height:877px;overflow:hidden;background:var(--white)}
body{font-family:"Outfit",sans-serif;color:var(--ink)}
.ad{position:relative;width:1200px;height:877px;overflow:hidden;background:var(--white)}
.backdrop{position:absolute;left:0;top:0;width:1200px;height:752px;
  background:linear-gradient(90deg,#e6e5e3 0%,#f6f6f5 25%,#e9e8e6 50%,#f5f5f4 75%,#e4e3e1 100%)}

/* brand */
.brand{position:absolute;left:45px;top:96px;display:flex;align-items:center;gap:16px}
.brand-mark{width:62px;height:62px;background:var(--gold)}
.brand-name{font-size:60px;font-weight:600;letter-spacing:4px;color:var(--gold-deep);line-height:1}
.brand-tagline{position:absolute;left:183px;top:185px;font-size:19px;font-weight:700;letter-spacing:1px;color:var(--muted)}

.attorney-tab{position:absolute;left:606px;top:181px;width:300px;height:45px;background:var(--gold);
  clip-path:polygon(26px 0,100% 0,100% 100%,0 100%)}
.attorney-name{position:absolute;left:648px;top:190px;font-size:21px;font-weight:600;color:var(--ink)}

/* practice band */
.practices{position:absolute;left:0;top:228px;width:1200px;height:99px;background:var(--ink);color:var(--white);
  font-size:26px;font-weight:500;text-align:center;padding:12px 300px 0 0;line-height:37px}
.practices span.sep{margin:0 11px}

/* contact band */
.contact{position:absolute;left:0;top:327px;width:1200px;height:86px;background:var(--gold-band)}
.contact-item{position:absolute;display:flex;align-items:center;gap:8px;font-weight:600;color:var(--ink)}
.contact-phone{left:24px;top:24px;font-size:28px}
.contact-web{left:286px;top:24px;font-size:28px}
.contact-address{left:540px;top:20px;font-size:17px;line-height:22px}
.contact-item svg{flex:none}

.attorney-photo{position:absolute;left:880px;top:42px;width:300px;height:371px;
  background:linear-gradient(180deg,var(--photo-a),var(--photo-b));border-radius:110px 110px 0 0}

/* calendar */
.calendar{position:absolute;left:0;top:413px;width:1200px;height:339px}
.month{position:absolute;width:128px;text-align:center}
.month h3{font-size:13.5px;font-weight:500;color:var(--gold);letter-spacing:.3px;margin-bottom:8px}
.days{display:grid;grid-template-columns:repeat(7,16px);justify-content:center;font-size:11.5px;font-weight:500;line-height:14.5px}
.days i,.days b{font-style:normal;font-weight:500}
.days b{color:var(--sunday)}
.days .hd{font-weight:600}
.o1{grid-column-start:2}.o2{grid-column-start:3}.o3{grid-column-start:4}
.o4{grid-column-start:5}.o5{grid-column-start:6}.o6{grid-column-start:7}
.year{position:absolute;left:1186px;top:515px;width:14px;height:156px;background:var(--ink)}
.year-label{position:absolute;left:1078px;top:565px;width:130px;height:54px;text-align:center;
  font-size:52px;font-weight:800;line-height:54px;letter-spacing:-1px;transform:rotate(-90deg)}

/* footer */
.footer-lines{position:absolute;left:0;top:752px}
.trust{position:absolute;left:0;top:763px;width:367px;font-size:26px;font-weight:500;line-height:33px;text-align:right}
.trust-count{position:absolute;left:378px;top:764px;font-size:76px;font-weight:700;line-height:76px;letter-spacing:-2px}
.trust-unit{position:absolute;left:488px;top:803px;font-size:26px;font-weight:500;line-height:30px}

.badge{position:absolute}
.badge-round{left:681px;top:784px;width:54px;height:54px;border-radius:50%;background:#6b1a1a}
.badge-rating{left:750px;top:788px;width:75px;height:46px;border-radius:4px;background:var(--sunday)}
.badge-list{left:846px;top:783px;width:75px;height:56px;border-radius:4px;background:var(--gold-deep)}
.badge-accred{left:940px;top:792px;width:122px;height:40px;border-radius:4px;background:#1c6aa0}
.badge-seal{left:1089px;top:780px;width:62px;height:62px;border-radius:50%;background:#2b8fd6}
</style>
</head>
<body>
<div class="ad">
  <div class="backdrop" role="img" aria-label="Soft marble courthouse columns background"></div>

  <div class="brand">
    <div class="brand-mark"></div>
    <div class="brand-name">MORVAN LEGAL</div>
  </div>
  <div class="brand-tagline">STANDING FIRM FOR YOUR FUTURE</div>

  <div class="attorney-tab"></div>
  <div class="attorney-name">Dorian K. Morvan, Esq.</div>

  <div class="practices">
    <div>Personal Injury<span class="sep">|</span>Unlicensed Contractors<span class="sep">|</span>Legal Malpractice</div>
    <div>Medical Malpractice<span class="sep">|</span>Civil Litigation</div>
  </div>

  <div class="contact">
    <div class="contact-item contact-phone">
      <svg width="24" height="26" viewBox="0 0 24 26" aria-hidden="true"><path d="M6 2l4 5-2 3c1 3 4 6 7 8l3-2 4 4-3 4C10 24 2 14 3 5z" fill="none" stroke="#111" stroke-width="2" stroke-linejoin="round"/></svg>
      (888) 555-0142
    </div>
    <div class="contact-item contact-web">
      <svg width="26" height="26" viewBox="0 0 26 26" aria-hidden="true"><g fill="none" stroke="#111" stroke-width="1.8"><circle cx="13" cy="13" r="11"/><ellipse cx="13" cy="13" rx="5" ry="11"/><path d="M2 13h22M4 7h18M4 19h18"/></g></svg>
      morvanlegal.net
    </div>
    <div class="contact-item contact-address">
      <svg width="36" height="32" viewBox="0 0 36 32" aria-hidden="true"><path d="M18 2L2 16h5v14h8v-9h6v9h8V16h5z" fill="#111"/></svg>
      <div>2170 Larkmont Ave. | Suite 408<br>Crestfield, CA | 90377</div>
    </div>
  </div>

  <div class="attorney-photo" role="img" aria-label="Portrait of attorney Dorian K. Morvan in a grey suit"></div>

  <div class="calendar">
    <div class="month" style="left:57px;top:30px"><h3>JANUARY</h3><div class="days">
      <b class="hd">S</b><i class="hd">M</i><i class="hd">T</i><i class="hd">W</i><i class="hd">T</i><i class="hd">F</i><i class="hd">S</i>
      <i class="o1">1</i><i>2</i><i>3</i><i>4</i><i>5</i><i>6</i><b>7</b><i>8</i><i>9</i><i>10</i><i>11</i><i>12</i><i>13</i><b>14</b><i>15</i><i>16</i><i>17</i><i>18</i><i>19</i><i>20</i><b>21</b><i>22</i><i>23</i><i>24</i><i>25</i><i>26</i><i>27</i><b>28</b><i>29</i><i>30</i><i>31</i>
    </div></div>
    <div class="month" style="left:239px;top:30px"><h3>FEBRUARY</h3><div class="days">
      <b class="hd">S</b><i class="hd">M</i><i class="hd">T</i><i class="hd">W</i><i class="hd">T</i><i class="hd">F</i><i class="hd">S</i>
      <i class="o4">1</i><i>2</i><i>3</i><b>4</b><i>5</i><i>6</i><i>7</i><i>8</i><i>9</i><i>10</i><b>11</b><i>12</i><i>13</i><i>14</i><i>15</i><i>16</i><i>17</i><b>18</b><i>19</i><i>20</i><i>21</i><i>22</i><i>23</i><i>24</i><b>25</b><i>26</i><i>27</i><i>28</i>
    </div></div>
    <div class="month" style="left:422px;top:30px"><h3>MARCH</h3><div class="days">
      <b class="hd">S</b><i class="hd">M</i><i class="hd">T</i><i class="hd">W</i><i class="hd">T</i><i class="hd">F</i><i class="hd">S</i>
      <i class="o4">1</i><i>2</i><i>3</i><b>4</b><i>5</i><i>6</i><i>7</i><i>8</i><i>9</i><i>10</i><b>11</b><i>12</i><i>13</i><i>14</i><i>15</i><i>16</i><i>17</i><b>18</b><i>19</i><i>20</i><i>21</i><i>22</i><i>23</i><i>24</i><b>25</b><i>26</i><i>27</i><i>28</i><i>29</i><i>30</i><i>31</i>
    </div></div>
    <div class="month" style="left:604px;top:30px"><h3>APRIL</h3><div class="days">
      <b class="hd">S</b><i class="hd">M</i><i class="hd">T</i><i class="hd">W</i><i class="hd">T</i><i class="hd">F</i><i class="hd">S</i>
      <b>1</b><i>2</i><i>3</i><i>4</i><i>5</i><i>6</i><i>7</i><b>8</b><i>9</i><i>10</i><i>11</i><i>12</i><i>13</i><i>14</i><b>15</b><i>16</i><i>17</i><i>18</i><i>19</i><i>20</i><i>21</i><b>22</b><i>23</i><i>24</i><i>25</i><i>26</i><i>27</i><i>28</i><b>29</b><i>30</i>
    </div></div>
    <div class="month" style="left:786px;top:30px"><h3>MAY</h3><div class="days">
      <b class="hd">S</b><i class="hd">M</i><i class="hd">T</i><i class="hd">W</i><i class="hd">T</i><i class="hd">F</i><i class="hd">S</i>
      <i class="o2">1</i><i>2</i><i>3</i><i>4</i><i>5</i><b>6</b><i>7</i><i>8</i><i>9</i><i>10</i><i>11</i><i>12</i><b>13</b><i>14</i><i>15</i><i>16</i><i>17</i><i>18</i><i>19</i><b>20</b><i>21</i><i>22</i><i>23</i><i>24</i><i>25</i><i>26</i><b>27</b><i>28</i><i>29</i><i>30</i><i>31</i>
    </div></div>
    <div class="month" style="left:969px;top:30px"><h3>JUNE</h3><div class="days">
      <b class="hd">S</b><i class="hd">M</i><i class="hd">T</i><i class="hd">W</i><i class="hd">T</i><i class="hd">F</i><i class="hd">S</i>
      <i class="o5">1</i><i>2</i><b>3</b><i>4</i><i>5</i><i>6</i><i>7</i><i>8</i><i>9</i><b>10</b><i>11</i><i>12</i><i>13</i><i>14</i><i>15</i><i>16</i><b>17</b><i>18</i><i>19</i><i>20</i><i>21</i><i>22</i><i>23</i><b>24</b><i>25</i><i>26</i><i>27</i><i>28</i><i>29</i><i>30</i>
    </div></div>

    <div class="month" style="left:57px;top:194px"><h3>JULY</h3><div class="days">
      <b class="hd">S</b><i class="hd">M</i><i class="hd">T</i><i class="hd">W</i><i class="hd">T</i><i class="hd">F</i><i class="hd">S</i>
      <b>1</b><i>2</i><i>3</i><i>4</i><i>5</i><i>6</i><i>7</i><b>8</b><i>9</i><i>10</i><i>11</i><i>12</i><i>13</i><i>14</i><b>15</b><i>16</i><i>17</i><i>18</i><i>19</i><i>20</i><i>21</i><b>22</b><i>23</i><i>24</i><i>25</i><i>26</i><i>27</i><i>28</i><b>29</b><i>30</i><i>31</i>
    </div></div>
    <div class="month" style="left:239px;top:194px"><h3>AUGUST</h3><div class="days">
      <b class="hd">S</b><i class="hd">M</i><i class="hd">T</i><i class="hd">W</i><i class="hd">T</i><i class="hd">F</i><i class="hd">S</i>
      <i class="o3">1</i><i>2</i><i>3</i><i>4</i><b>5</b><i>6</i><i>7</i><i>8</i><i>9</i><i>10</i><i>11</i><b>12</b><i>13</i><i>14</i><i>15</i><i>16</i><i>17</i><i>18</i><b>19</b><i>20</i><i>21</i><i>22</i><i>23</i><i>24</i><i>25</i><b>26</b><i>27</i><i>28</i><i>29</i><i>30</i><i>31</i>
    </div></div>
    <div class="month" style="left:422px;top:194px"><h3>SEPTEMBER</h3><div class="days">
      <b class="hd">S</b><i class="hd">M</i><i class="hd">T</i><i class="hd">W</i><i class="hd">T</i><i class="hd">F</i><i class="hd">S</i>
      <i class="o6">1</i><b>2</b><i>3</i><i>4</i><i>5</i><i>6</i><i>7</i><i>8</i><b>9</b><i>10</i><i>11</i><i>12</i><i>13</i><i>14</i><i>15</i><b>16</b><i>17</i><i>18</i><i>19</i><i>20</i><i>21</i><i>22</i><b>23</b><i>24</i><i>25</i><i>26</i><i>27</i><i>28</i><i>29</i><b>30</b>
    </div></div>
    <div class="month" style="left:604px;top:194px"><h3>OCTOBER</h3><div class="days">
      <i class="hd">S</i><i class="hd">M</i><i class="hd">T</i><i class="hd">W</i><i class="hd">T</i><i class="hd">F</i><i class="hd">S</i>
      <i class="o1">1</i><i>2</i><i>3</i><i>4</i><i>5</i><i>6</i><i>7</i><i>8</i><i>9</i><i>10</i><i>11</i><i>12</i><i>13</i><i>14</i><i>15</i><i>16</i><i>17</i><i>18</i><i>19</i><i>20</i><i>21</i><i>22</i><i>23</i><i>24</i><i>25</i><i>26</i><i>27</i><i>28</i><i>29</i><i>30</i><i>31</i>
    </div></div>
    <div class="month" style="left:786px;top:194px"><h3>NOVEMBER</h3><div class="days">
      <b class="hd">S</b><i class="hd">M</i><i class="hd">T</i><i class="hd">W</i><i class="hd">T</i><i class="hd">F</i><i class="hd">S</i>
      <i class="o4">1</i><i>2</i><i>3</i><b>4</b><i>5</i><i>6</i><i>7</i><i>8</i><i>9</i><i>10</i><b>11</b><i>12</i><i>13</i><i>14</i><i>15</i><i>16</i><i>17</i><b>18</b><i>19</i><i>20</i><i>21</i><i>22</i><i>23</i><i>24</i><b>25</b><i>26</i><i>27</i><i>28</i><i>29</i><i>30</i>
    </div></div>
    <div class="month" style="left:969px;top:194px"><h3>DECEMBER</h3><div class="days">
      <b class="hd">S</b><i class="hd">M</i><i class="hd">T</i><i class="hd">W</i><i class="hd">T</i><i class="hd">F</i><i class="hd">S</i>
      <i class="o6">1</i><b>2</b><i>3</i><i>4</i><i>5</i><i>6</i><i>7</i><i>8</i><b>9</b><i>10</i><i>11</i><i>12</i><i>13</i><i>14</i><i>15</i><b>16</b><i>17</i><i>18</i><i>19</i><i>20</i><i>21</i><i>22</i><b>23</b><i>24</i><i>25</i><i>26</i><i>27</i><i>28</i><i>29</i><b>30</b><i>31</i>
    </div></div>
  </div>

  <div class="year"></div>
  <div class="year-label">2018</div>

  <svg class="footer-lines" width="1200" height="125" viewBox="0 0 1200 125" aria-hidden="true">
    <rect x="0" y="0" width="1200" height="125" fill="#ffffff"/>
    <polygon points="678,0 1200,0 1200,10 672,10" fill="#111"/>
    <polygon points="0,87 604,87 597,98 0,98" fill="#111"/>
    <polygon points="590,98 605,98 646,24 631,24" fill="#111"/>
  </svg>

  <div class="trust">Known and Trusted in<br>Our Community for over</div>
  <div class="trust-count">22</div>
  <div class="trust-unit">Years</div>

  <div class="badge badge-round"></div>
  <div class="badge badge-rating"></div>
  <div class="badge badge-list"></div>
  <div class="badge badge-accred"></div>
  <div class="badge badge-seal"></div>
</div>
</body>
</html>
```